Vitra-Montalis Flyer Patient Day

We need a flyer for an event (format A5, double-sided, portrait format). This event is aimed at lymphology patients. The aim of this case is to inform patients about the progress of treatment, to show trends and to get in touch with them. The structure of the Flyer must be follows: - Page 1: with the title and date and logo of Vitra-Montalis - Page 2: with info text and details of the event The text templates are attached below: (180216_VA_Briefing_Workshopflyer_Betroffenentag_Vitra-Montalis.docx) The logos for the partners are also attached below. The following design inputs: 1) Please visit the following website: www.vitra-montalis.ch and use the logo of Vitra-Montalis 2) The visual language should be appropriate for the theme of networking (No Go people, preferably using graphical elements. ) Please use elements of the lymphology pathways, 3) For texts please use the following font: Roboto-Light For running text please use the following font: PT-Serif-Italic, sans-serif 4) The texts must be reader-friendly Please note that this flyer is not for Peravin, but for Vitra-Montalis.

```html
<!DOCTYPE html>
<html lang="de">
<head>
<meta charset="utf-8">
<title>Vitra-Montalis – Betroffenentag Flyer</title>
<link href="https://fonts.googleapis.com/css2?family=Roboto:wght@300;400&display=swap" rel="stylesheet">
<style>
  :root{
    --bg:#85857a;
    --paper:#ffffff;
    --green-light:#c9e07a;
    --green:#8fbf35;
    --green-deep:#5f9a25;
    --orange:#f08a1c;
    --yellow:#f7c21e;
    --text:#3a3a3a;
    --muted:#6a6a6a;
    --footer:#ececec;
    --navy:#1c2a4a;
  }
  *{box-sizing:border-box;margin:0;padding:0}
  html,body{width:1200px;height:924px;overflow:hidden}
  body{background:var(--bg);font-family:"Roboto",Arial,sans-serif;font-weight:300;color:var(--text);position:relative}

  .page{position:absolute;top:108px;width:500px;height:708px;background:var(--paper);overflow:hidden;box-shadow:0 8px 24px rgba(0,0,0,.25)}
  .page--back{left:70px}
  .page--front{left:630px}

  /* Back page */
  .intro{position:absolute;left:0;top:0;width:100%;height:137px;
    background:linear-gradient(180deg,var(--green-light) 0%,var(--green) 100%)}
  .intro__text{position:absolute;left:56px;right:56px;top:36px;font-size:14px;line-height:21px;color:#f4f8e6;text-align:justify}

  .details{position:absolute;left:34px;top:176px;width:200px;font-size:13px;line-height:17px}
  .programme{position:absolute;left:244px;top:176px;width:240px;font-size:13px;line-height:17px}
  .label{display:inline-block;padding:0 6px;border-radius:4px 0 4px 0;color:#fff;font-size:13px;line-height:15px;
    background:linear-gradient(90deg,var(--orange),var(--yellow))}
  .field{margin-bottom:18px}
  .field p{padding-left:8px}
  .field--inline p{display:inline;padding-left:2px}
  .programme ul{list-style:none;margin-top:2px}
  .programme li{position:relative;padding-left:10px}
  .programme li::before{content:"";position:absolute;left:1px;top:7px;width:4px;height:4px;border-radius:50%;background:var(--orange)}
  .programme li.sub{padding-left:24px}
  .programme li.sub::before{left:20px;width:2px;height:2px;background:var(--text)}

  .fees{position:absolute;left:42px;top:444px;width:420px;font-size:13.5px;line-height:17px}
  .contact{position:absolute;left:42px;top:504px;font-size:13.5px;line-height:19px}
  .contact__mail{display:flex;align-items:center;gap:5px}

  .deadline{position:absolute;left:308px;top:478px;width:104px;height:54px;border:2px solid #9fd3e0;background:#f4fbfd}
  .deadline__head{background:#9fd3e0;color:#fff;font-size:11px;line-height:13px;padding-left:6px}
  .deadline__body{display:flex;align-items:center;padding-left:6px;color:var(--orange)}
  .deadline__day{font-size:32px;line-height:36px}
  .deadline__month{font-size:12px;line-height:12px;margin-left:3px}
  .deadline__pen{position:absolute;right:-14px;top:-14px}

  .partners{position:absolute;left:40px;right:40px;top:574px;text-align:center}
  .partners__title{display:flex;align-items:center;gap:12px;font-size:13px;color:var(--muted);justify-content:center}
  .partners__title::before,.partners__title::after{content:"";flex:1;height:2px;background:linear-gradient(90deg,transparent,#c8c8c8)}
  .partners__title::after{transform:scaleX(-1)}
  .partners__row{display:flex;justify-content:space-around;align-items:center;margin-top:16px;font-size:18px}
  .partner--a{color:#1b3d8f}
  .partner--b{color:#5b2a86}
  .partner--c{background:var(--navy);color:#fff;font-size:11px;padding:8px 6px;letter-spacing:.5px}
  .partner--d{color:#1f4ea1;font-size:20px}

  .footer{position:absolute;left:0;bottom:0;width:100%;height:74px;background:var(--footer);text-align:center;padding-top:14px}
  .footer__address{font-size:15px;line-height:20px}
  .footer__meta{font-size:11.5px;margin-top:6px;color:var(--text)}

  /* Front page */
  .landscape{position:absolute;left:0;top:58px;width:100%;height:460px;
    background:linear-gradient(180deg,#e7efc2 0%,var(--green) 18%,#7fb32f 45%,#a3cc55 72%,rgba(255,255,255,0) 100%)}
  .brand{position:absolute;right:40px;top:30px;display:flex;align-items:center;gap:8px;background:#fff;padding:10px 12px;font-size:19px;color:#222}
  .brand__mark{width:12px;height:12px;background:var(--green)}
  .title{position:absolute;left:52px;top:208px;color:#fff;font-size:27px;line-height:27px}
  .date{position:absolute;left:60px;top:316px;display:flex;align-items:center;color:#fff}
  .date__day{font-size:44px;line-height:44px}
  .date__month{color:var(--yellow);font-size:19px;line-height:17px;margin-left:4px}

  .assoc{position:absolute;left:70px;top:528px;display:flex;align-items:center;gap:22px}
  .assoc__mark{width:26px;height:26px;border-radius:50%;background:var(--green-deep)}
  .assoc__names{font-size:18px;line-height:21px;color:#222}
  .lv{position:absolute;left:44px;bottom:30px;font-size:10px;line-height:12px;color:#222;display:flex;align-items:center;gap:6px}
  .lv__mark{width:10px;height:10px;border-radius:50%;background:#d4d4d4}
  .lv strong{font-weight:400}
  .website{position:absolute;right:40px;bottom:34px;font-size:12px;color:#1f4ea1}
</style>
</head>
<body>

<section class="page page--back">
  <div class="intro" role="img" aria-label="Luftaufnahme einer grünen Flusslandschaft mit verzweigten Wasserläufen">
    <p class="intro__text">Die Stiftung Vitra-Montalis organisiert mit den beiden Betroffenenorganisationen Vereinigung Lipödem Alpenland und Lymphödem Verband Alpenland die folgende Tagung:</p>
  </div>

  <div class="details">
    <div class="field field--inline"><span class="label">Datum</span> <p>16. Juni 2018</p></div>
    <div class="field"><span class="label">Zeit</span>
      <p>ab 9h00 Eintreffen der Besucher (Industrieausstellung geöffnet) ab 10h00 Start des Tagungsprogramms</p></div>
    <div class="field field--inline"><span class="label">Ort</span> <p>TBD, Aarau</p></div>
    <div class="field"><span class="label">Zielgruppe</span><p>Betroffene und Angehörige</p></div>
    <div class="field"><span class="label">Eintritt</span></div>
  </div>

  <div class="programme">
    <span class="label">Programme</span>
    <ul>
      <li>Industrieausstellung</li>
      <li>Darstellung Lip- und Lymphödem</li>
      <li>Vorstellung der Organisationen</li>
      <li class="sub">Stiftung Vitra-Montalis</li>
      <li class="sub">Vereinigung Lipödem Alpenland</li>
      <li class="sub">Lymphödem Verband Alpenland</li>
      <li>Ausgewogene Ernährung</li>
      <li>Mode für Betroffene</li>
      <li>Sport als Bestandteil der Therapie</li>
    </ul>
  </div>

  <p class="fees">Teilnahmegebühren inkl. Mittagessen CHF 50.- pro Person, jede weitere Person CHF 15.-</p>

  <div class="contact">
    <p>Anmeldungen und Fragen via</p>
    <p class="contact__mail">
      <svg width="20" height="15" viewBox="0 0 20 15" aria-hidden="true"><rect x="1" y="1" width="18" height="13" fill="none" stroke="#f08a1c" stroke-width="1.4"/><path d="M1 1l9 7 9-7" fill="none" stroke="#f08a1c" stroke-width="1.4"/></svg>
      info@vitra-montalis.ch</p>
  </div>

  <div class="deadline">
    <div class="deadline__head">Anmeldefrist</div>
    <div class="deadline__body"><span class="deadline__day">20</span><span class="deadline__month">Mai<br>2018</span></div>
    <svg class="deadline__pen" width="30" height="30" viewBox="0 0 30 30" aria-hidden="true"><path d="M4 26l3-8 15-15 5 5-15 15z" fill="#fff" stroke="#9fd3e0" stroke-width="2"/></svg>
  </div>

  <div class="partners">
    <div class="partners__title">PARTNER</div>
    <div class="partners__row">
      <span class="partner--a">Medora</span>
      <span class="partner--b">peravin</span>
      <span class="partner--c">TESSALIN</span>
      <span class="partner--d">KORVEL</span>
    </div>
  </div>

  <footer class="footer">
    <p class="footer__address">Stiftung Vitra-Montalis Talstrasse 12 CH-3900 Brig</p>
    <p class="footer__meta">+41 76 000 12 34 &nbsp;|&nbsp; info@vitra-montalis.ch &nbsp;|&nbsp; www.vitra-montalis.ch</p>
  </footer>
</section>

<section class="page page--front">
  <div class="landscape" role="img" aria-label="Luftaufnahme einer grünen Flusslandschaft mit verzweigten Wasserläufen, nach unten in Weiss übergehend"></div>
  <div class="brand"><span class="brand__mark"></span>Vitra-Montalis</div>
  <h1 class="title" style="font-weight:300">Betroffenen- und<br>Angehörigentag Lip- und<br>Lymphödem</h1>
  <div class="date"><span class="date__day">16</span><span class="date__month">Jun<br>2018</span></div>

  <div class="assoc">
    <span class="assoc__mark"></span>
    <p class="assoc__names">vereinigung lipödem alpenland<br>association lipoedème alpine<br>associazione lipedema alpina<br>alpine lipoedema association</p>
  </div>

  <div class="lv"><span class="lv__mark"></span><p><strong>LV-Alpenland</strong><br>Lymphödem Verband Alpenland</p></div>
  <p class="website">www.vitra-montalis.ch</p>
</section>

</body>
</html>
```